Group fitness classes - DL flyer

We need a flyer design for our boutique fitness studio.

We would prefer to see the use of pictures in the design.

One sided. Please allow space around the edges for bleed.

Flyer should have the following text:

Harwell Motion Loft
Group fitness special – two weeks unlimited group fitness classes for $29*
Enjoy unlimited access to our fantastic group classes including PulseRun, Yoga, Strength Circuit and Self Defence Martial Arts.
Purchase your pass through our online store by selecting the "Special Offers" option.
Bring this flyer to your first class and receive an extra two weeks free!

www.harwellmotionloft.com.au
or phone
0482 *** ***
4/63 Birchwood Lane Flemington

*New clients only

Industry/Entity Type

Boutique

Font styles to use
Serif
Sans Serif

Requirements
Must have
• Photos
Should not have
• Cartoons

```html
<!DOCTYPE html>
<html lang="en">
<head>
<meta charset="utf-8">
<title>Harwell Motion Loft – Group Fitness Flyer</title>
<link href="https://fonts.googleapis.com/css2?family=Open+Sans:wght@400;600;700;800&family=Roboto+Condensed:ital,wght@0,700;1,700&display=swap" rel="stylesheet">
<style>
  :root{
    --page-bg:#e6e7e9;
    --paper:#ffffff;
    --navy:#1e2b3a;
    --ink:#333a42;
    --blue:#1c9fdf;
    --blue-deep:#0f72bb;
    --blue-light:#5fc4f0;
    --badge:#151515;
    --accent-yellow:#ffe14a;
  }
  *{box-sizing:border-box;margin:0;padding:0}
  html,body{width:1200px;height:1040px;overflow:hidden;background:var(--page-bg)}
  .flyer{
    position:absolute;left:50px;top:129px;width:1100px;height:782px;
    background:var(--paper);
    box-shadow:0 6px 24px rgba(0,0,0,.18);
    font-family:"Open Sans",Arial,sans-serif;
  }
  .flyer-art{position:absolute;left:0;top:0;width:1100px;height:782px}
  .offer-badge{
    position:absolute;left:12px;top:30px;width:258px;height:186px;
    transform:rotate(-9deg);
    display:flex;flex-direction:column;align-items:center;justify-content:center;
    color:#fff;text-align:center;
    font-family:"Roboto Condensed",Arial,sans-serif;font-weight:700;
    font-size:15px;line-height:1.15;letter-spacing:.2px;text-transform:uppercase;
  }
  .offer-badge .price{font-size:54px;line-height:1;margin-top:6px}
  .offer-badge .price sup{font-size:22px;vertical-align:top;position:relative;top:6px}
  .headline{
    position:absolute;left:292px;top:92px;width:800px;
    color:var(--navy);font-weight:700;font-size:28px;line-height:1.35;letter-spacing:-.3px;
  }
  .headline .tag{
    background:var(--blue);color:#fff;padding:0 8px;border-radius:3px;
  }
  .class-list{
    position:absolute;left:38px;top:590px;width:330px;color:#fff;
    font-size:19px;line-height:1.28;
  }
  .class-list ul{list-style:none;margin-top:8px;font-weight:800;font-size:21px;line-height:1.2}
  .class-list li{display:inline}
  .class-list li::before{content:"•";color:var(--accent-yellow);margin-right:4px}
  .class-list li.block{display:block}
  .bonus{
    position:absolute;left:406px;top:676px;width:370px;
    color:var(--blue);font-family:"Roboto Condensed",Arial,sans-serif;
    font-style:italic;font-weight:700;font-size:20px;line-height:1.25;text-transform:uppercase;
  }
  .divider{position:absolute;left:786px;top:640px;width:2px;height:120px;background:#b9bdc2}
  .studio-name{
    position:absolute;left:808px;top:584px;display:flex;align-items:center;gap:10px;
    color:var(--ink);font-family:"Roboto Condensed",Arial,sans-serif;font-weight:700;
    font-size:25px;letter-spacing:.5px;text-transform:uppercase;
  }
  .studio-name .dot{width:16px;height:16px;border-radius:50%;background:var(--blue)}
  .studio-contact{position:absolute;left:808px;top:668px;color:var(--ink)}
  .studio-contact .address{font-size:15px;line-height:1.35}
  .studio-contact .phone{font-size:32px;font-weight:700;margin-top:4px;color:var(--navy)}
</style>
</head>
<body>
<main class="flyer">
  <svg class="flyer-art" viewBox="0 0 1100 782" xmlns="http://www.w3.org/2000/svg">
    <defs>
      <linearGradient id="photoTone" x1="0" y1="0" x2="0" y2="1">
        <stop offset="0" stop-color="#d9dde0"/>
        <stop offset=".28" stop-color="#9fb4bc"/>
        <stop offset=".5" stop-color="#2f95ab"/>
        <stop offset=".75" stop-color="#3b5f6d"/>
        <stop offset="1" stop-color="#8a5a3c"/>
      </linearGradient>
      <linearGradient id="panelBlue" x1="0" y1="0" x2="0" y2="1">
        <stop offset="0" stop-color="var(--blue-light)"/>
        <stop offset="1" stop-color="var(--blue-deep)"/>
      </linearGradient>
    </defs>
    <path role="img" aria-label="Photo of a group fitness class lifting barbells overhead in a bright studio"
      d="M13,30 Q13,13 30,13 H1070 Q1087,13 1087,30 V336 C900,470 620,600 379,626 V769 H30 Q13,769 13,752 Z"
      fill="url(#photoTone)"/>
    <path d="M1087,336 C900,470 620,600 379,626" fill="none" stroke="var(--blue)" stroke-width="14"/>
    <path d="M1087,350 C900,486 620,614 379,640" fill="none" stroke="var(--blue-light)" stroke-width="3"/>
    <path d="M13,566 H330 Q379,566 379,612 V769 H30 Q13,769 13,752 Z" fill="url(#panelBlue)"/>
    <ellipse cx="141" cy="123" rx="132" ry="92" transform="rotate(-9 141 123)" fill="var(--badge)"/>
  </svg>

  <div class="offer-badge">
    <span>Group fitness special<br>two weeks unlimited<br>group fitness classes for</span>
    <span class="price">$29<sup>*</sup></span>
  </div>

  <p class="headline">Purchase your pass through our online store by selecting the<br><span class="tag">Special Offers</span> option.</p>

  <div class="class-list">
    <p>Enjoy unlimited access to our fantastic group classes including</p>
    <ul>
      <li>PulseRun</li> <li>Yoga</li>
      <li class="block">Strength Circuit and</li>
      <li class="block">Self Defense Martial Arts.</li>
    </ul>
  </div>

  <p class="bonus">Bring this flyer to your first class and receive an extra two weeks free!</p>

  <div class="divider"></div>

  <div class="studio-name"><span class="dot"></span>Harwell Motion Loft</div>
  <div class="studio-contact">
    <p class="address">Harwell Motion Loft,<br>4/63 Birchwood Lane, Flemington.</p>
    <p class="phone">0482 *** ***</p>
  </div>
</main>
</body>
</html>
```